Courier Business needs a Business Card Design !!!

My new company needs a business card design. Our company name is Maple Dart Courier & Delivery Services. We will be servicing residential , government and business clients in the City of Yellowknife, Northwest Territories, Canada. I would like the following information included on the card: Name- Calvin Oxley. Title- Owner. Company- Maple Dart Courier & Delivery Services. Address- PO Box 5918 , Yellowknife , NWT, X0E 4K3. Phone- 867-555-0193. Email- mapledartdelivery@postfern.example. Facebook- www.socialpage.example/mapledartdelivery. I would like my double sided card to be the standard size of 84mm x 55mm. No borders. Use CMYK mode.1039x 697 pixels at least. I would like my logo to take up at least one quarter of the area of one side of the card. Text should be at least 8 point with perhaps my name being 10 point and my company name being 12-15 point . It should have clear readable font. Please use one or two bold colors. I am trying to attract the business community so a professional look might be best. My tag line is " On Time Every Time ". Nice safe margins please. We will be providing fast, reliable and professional delivery of envelopes and small packages within the City of Yellowknife. We offer 100% satisfaction or a complete refund. I have included a file of our logo. I like black, blue and red but am willing to look at what you feel would work best. I do not really like white as a background color.

Target Market(s)

Professionals , business owners. 30-50 years old

Industry/Entity Type

Residential

Contact Information for Business Card

As noted in brief

Font styles to use
Serif
Sans Serif

Colors
000000
0255a3
f04a50

Requirements
Must have
• My contact info. My logo
Nice to have
• Simple elegant design but still catches the eye
Should not have
• White background color

```html
<!DOCTYPE html>
<html lang="en">
<head>
<meta charset="utf-8">
<title>Maple Dart Courier &amp; Delivery Services – Business Card</title>
<link href="https://fonts.googleapis.com/css2?family=Open+Sans:ital,wdth,wght@0,75..100,300..800;1,75..100,300..800&display=swap" rel="stylesheet">
<style>
  :root {
    --coral: #f04a50;
    --white: #ffffff;
    --trim: #6fd3e0;
    --tag-yellow: #e8e21a;
    --page: #ffffff;
  }
  * { margin: 0; padding: 0; box-sizing: border-box; }
  html, body {
    width: 1200px; height: 1000px; overflow: hidden;
    background: var(--page);
    font-family: "Open Sans", Arial, sans-serif;
  }
  .card {
    position: absolute;
    left: 100px; top: 178px;
    width: 1002px; height: 650px;
    border: 1px solid var(--trim);
    background: var(--white);
  }
  .contact-band {
    position: absolute;
    left: 0; top: 0;
    width: 100%; height: 226px;
    background: var(--coral);
    color: var(--white);
  }
  .holder {
    position: absolute;
    left: 18px; top: 38px;
    width: 340px;
    font-style: italic;
    font-weight: 400;
  }
  .holder-name {
    font-size: 58px;
    line-height: 54px;
    letter-spacing: -0.5px;
  }
  .holder-name span { display: block; }
  .holder-name .surname { padding-left: 14px; }
  .holder-title {
    font-size: 40px;
    line-height: 40px;
    text-align: right;
    margin-top: -4px;
    margin-right: -8px;
  }
  .contact-list {
    position: absolute;
    left: 390px; top: 42px;
    list-style: none;
    font-size: 26.5px;
    line-height: 39.5px;
    white-space: nowrap;
  }
  .brand {
    position: absolute;
    left: 88px; top: 318px;
    width: 830px;
    color: var(--coral);
    font-weight: 800;
    font-stretch: 75%;
    text-transform: uppercase;
    line-height: 1;
  }
  .brand-name { font-size: 112px; letter-spacing: 1px; }
  .brand-line { font-size: 62px; letter-spacing: 0.5px; margin-top: 6px; }
  .tagline-band {
    position: absolute;
    left: 93px; top: 540px;
    width: 820px; height: 50px;
    background: var(--coral);
    display: flex; align-items: center; justify-content: center;
  }
  .tagline {
    color: var(--tag-yellow);
    font-size: 25px;
    font-weight: 400;
    letter-spacing: 9px;
    text-transform: uppercase;
    margin-left: -200px;
  }
</style>
</head>
<body>
  <article class="card">
    <header class="contact-band">
      <div class="holder">
        <p class="holder-name"><span>Calvin</span><span class="surname">Oxley</span></p>
        <p class="holder-title">Owner</p>
      </div>
      <ul class="contact-list">
        <li>PO Box 5918, Yellowknife, NWT, X0E 4K3.</li>
        <li>867-555-0193</li>
        <li>mapledartdelivery@postfern.example</li>
        <li>www.socialpage.example/mapledartdelivery</li>
      </ul>
    </header>
    <div class="brand">
      <p class="brand-name">Maple Dart</p>
      <p class="brand-line">Courier &amp; Delivery Services</p>
    </div>
    <div class="tagline-band">
      <p class="tagline">On Time Every Time</p>
    </div>
  </article>
</body>
</html>
```